Quillmark painting

Am looking for a lawn sign design for my paintings company.
I also attached my business card a example

Phone number of the business +1(204)555-0187
Key words:Free estimates|pressure washing |Residential| Commercial | Interior | Exterior

```html
<!DOCTYPE html>
<html lang="en">
<head>
<meta charset="utf-8">
<title>Quillmark painting lawn sign</title>
<link rel="stylesheet" href="https://fonts.googleapis.com/css2?family=Montserrat:wght@700;800&family=Oswald:wght@500&display=swap">
<style>
  :root {
    --page: #eceeea;
    --frame-yellow: #f2e20f;
    --frame-green: #7cc242;
    --white: #ffffff;
    --sky: #1ea6df;
    --ink: #1d1d1f;
    --divider: #7cc242;
    --band: #2e2e86;
    --name-yellow: #f2e20f;
    --icon-green: #6cbf45;
  }
  * { box-sizing: border-box; margin: 0; padding: 0; }
  html, body { width: 1200px; height: 1117px; overflow: hidden; }
  body { background: var(--page); font-family: "Montserrat", Arial, sans-serif; }

  .lawn-sign {
    position: absolute; left: 40px; top: 153px;
    width: 1120px; height: 810px;
    padding: 18px;
    background: linear-gradient(45deg, var(--frame-yellow) 0%, var(--frame-green) 55%, var(--frame-green) 100%);
  }
  .sign-face {
    position: relative; width: 100%; height: 100%;
    background: var(--white); overflow: hidden;
  }

  .splash-top {
    position: absolute; left: 40px; top: 8px; width: 620px; height: 120px;
    background: radial-gradient(ellipse at 20% 40%, rgba(30,110,200,.55), transparent 45%),
                radial-gradient(ellipse at 50% 50%, rgba(236,110,170,.5), transparent 55%),
                radial-gradient(ellipse at 80% 40%, rgba(248,170,60,.55), transparent 50%);
    filter: blur(6px);
  }
  .splash-corner {
    position: absolute; right: 8px; top: 520px; width: 330px; height: 170px;
    background: radial-gradient(ellipse at 30% 55%, rgba(140,200,60,.75), transparent 55%),
                radial-gradient(ellipse at 75% 65%, rgba(236,80,150,.75), transparent 50%),
                radial-gradient(ellipse at 85% 20%, rgba(110,90,200,.5), transparent 35%);
    filter: blur(5px);
  }

  .brand-name {
    position: absolute; left: 0; right: 0; top: 110px;
    text-align: center; color: var(--sky);
    font-family: "Montserrat", Arial, sans-serif; font-weight: 800;
    font-size: 148px; line-height: 1; letter-spacing: -2px; text-transform: uppercase;
  }
  .brand-name .brand-sub { display: block; font-size: 60px; letter-spacing: 18px; margin-top: 8px; }

  .services {
    position: absolute; left: 100px; right: 100px; top: 418px;
    text-align: center; color: var(--ink);
    font-weight: 700; font-size: 33px; line-height: 48px;
  }
  .services .sep { color: var(--divider); margin: 0 6px; }

  .contact-band {
    position: absolute; left: 0; right: 0; bottom: 0; height: 180px;
    background: var(--band);
  }
  .contact-name {
    position: absolute; left: 120px; top: 24px;
    color: var(--name-yellow); font-weight: 800; font-size: 34px; letter-spacing: 3px;
  }
  .contact-row {
    position: absolute; left: 66px; top: 84px;
    display: flex; align-items: center; gap: 14px;
    color: var(--white); font-family: "Oswald", Arial, sans-serif; font-weight: 500; font-size: 46px;
  }
  .contact-row .bar { margin: 0 12px; }
  .icon { width: 38px; height: 38px; flex: none; }
</style>
</head>
<body>
  <div class="lawn-sign">
    <div class="sign-face">
      <div class="splash-top" role="img" aria-label="Watercolour paint splash in blue, pink and orange"></div>
      <div class="splash-corner" role="img" aria-label="Watercolour paint splash in green, pink and violet"></div>

      <h1 class="brand-name">Quillmark<span class="brand-sub">painting</span></h1>

      <p class="services">
        Free estimates<span class="sep">|</span>pressure<br>
        washing<span class="sep">|</span>Residential<span class="sep">|</span>Commercial<span class="sep">|</span><br>
        Interior<span class="sep">|</span>Exterior
      </p>

      <div class="contact-band">
        <div class="contact-name">Marco</div>
        <div class="contact-row">
          <svg class="icon" viewBox="0 0 40 40" aria-hidden="true">
            <circle cx="20" cy="20" r="20" fill="var(--icon-green)"/>
            <path d="M13 11c1-1 2-1 3 0l3 4c.6.8.4 1.8-.3 2.4l-1.4 1.2c1.2 2.5 3 4.4 5.4 5.6l1.3-1.4c.6-.7 1.6-.8 2.4-.2l4 3c1 .8 1 2 0 3l-1.5 1.6c-1.5 1.5-4 1.4-7-.3-4.5-2.5-8-6.5-10-11-1.3-3-1.2-5.4.2-6.8z" fill="var(--band)"/>
          </svg>
          <span class="phone">+1(204)555-0187</span>
          <span class="bar">|</span>
          <svg class="icon" viewBox="0 0 40 40" aria-hidden="true">
            <circle cx="20" cy="20" r="20" fill="var(--icon-green)"/>
            <g fill="none" stroke="var(--band)" stroke-width="2">
              <circle cx="20" cy="20" r="10"/>
              <ellipse cx="20" cy="20" rx="4.5" ry="10"/>
              <line x1="10" y1="20" x2="30" y2="20"/>
              <line x1="12" y1="14.5" x2="28" y2="14.5"/>
              <line x1="12" y1="25.5" x2="28" y2="25.5"/>
            </g>
          </svg>
          <span class="email">hello@quillmarkpaint.ca</span>
        </div>
      </div>
    </div>
  </div>
</body>
</html>
```